coaching agenda

Please redesign the brochure attached in a more modern/trendy out look. I want something completely different to what is attached but using the same colours and logo.

```html
<!DOCTYPE html>
<html lang="en">
<head>
<meta charset="utf-8">
<title>Coaching Session – June 2018</title>
<link href="https://fonts.googleapis.com/css2?family=Montserrat:wght@500;700;800&family=Arimo:wght@400;700&display=swap" rel="stylesheet">
<style>
:root{
  --stage:#3b3b3b;
  --paper:#ffffff;
  --brand-blue:#1ba3dc;
  --ink:#2f2f2f;
  --ink-soft:#555a5e;
  --dark-band:#3a3d40;
  --grey-disc:#cfd0d1;
  --photo-light:#eeeeee;
  --photo-mid:#d4d4d4;
}
*{box-sizing:border-box;margin:0;padding:0}
html,body{width:1004px;height:1200px;overflow:hidden;background:var(--stage)}
body{position:relative;font-family:"Arimo",Arial,sans-serif;color:var(--ink)}
.spread{position:absolute;left:106px;width:792px;height:560px;display:flex;box-shadow:0 10px 30px rgba(0,0,0,.45)}
.spread--cover{top:20px}
.spread--inner{top:620px}
.page{position:relative;width:396px;height:560px;background:var(--paper);overflow:hidden}
.page--left{background:linear-gradient(90deg,#fff 80%,#ececec 100%)}
.page--right{background:linear-gradient(90deg,#ececec 0%,#fff 12%)}
.page svg.layer{position:absolute;inset:0}

/* name mark */
.namemark{display:flex;align-items:center;gap:6px;font-family:"Montserrat",sans-serif;font-weight:700;color:var(--ink)}
.namemark__square{width:9px;height:9px;background:var(--brand-blue)}
.namemark--large{position:absolute;left:120px;top:40px;font-size:15px}
.namemark__sub{position:absolute;left:135px;top:62px;font-size:5.5px;color:var(--ink-soft);letter-spacing:.3px}
.namemark--small{font-size:8px}
.namemark--small .namemark__square{width:6px;height:6px}

/* cover front */
.cover-title{position:absolute;left:188px;top:332px;background:var(--brand-blue);color:#fff;font-family:"Montserrat",sans-serif;font-weight:800;font-size:13px;letter-spacing:.4px;padding:5px 10px}
.cover-date{position:absolute;left:202px;top:365px;background:var(--dark-band);color:#fff;font-family:"Montserrat",sans-serif;font-weight:600;font-size:9px;padding:4px 12px}
.cover-url{position:absolute;left:210px;top:410px;font-size:8px;color:var(--ink)}

/* back cover contacts */
.contact-bar{position:absolute;left:36px;right:20px;bottom:40px;display:flex;align-items:flex-end;gap:18px}
.contact-list{list-style:none;font-size:7px;line-height:11px;color:var(--ink)}
.contact-list li{display:flex;align-items:center;gap:4px}
.contact-list svg{width:8px;height:8px;flex:none}

/* inner pages */
.copy{position:absolute;font-size:7.4px;line-height:10px;color:var(--ink-soft)}
.copy h2{font-family:"Montserrat",sans-serif;font-weight:800;color:var(--brand-blue);font-size:12.5px;line-height:15px}
.copy h3{font-family:"Montserrat",sans-serif;font-weight:700;color:var(--ink);font-size:7.6px;margin:1px 0 3px}
.copy p.lead{font-family:"Montserrat",sans-serif;font-weight:700;color:var(--ink);font-size:7.4px;line-height:10px}
.numbered{list-style:none}
.numbered li{display:flex;gap:10px;margin-bottom:3.4px}
.numbered li b{color:var(--brand-blue);width:10px;flex:none;font-weight:700}
.copy-left{left:34px;top:26px;width:340px}
.copy-left section{margin-bottom:10px}
.copy-right{left:22px;top:22px;width:232px}
.copy-right .lead{margin-bottom:8px}
.bullets{display:grid;grid-template-columns:1fr 1fr;gap:0 8px;margin:4px 0 8px}
.bullets ul{list-style:none}
.bullets li{position:relative;padding-left:8px;margin-bottom:4.6px}
.bullets li::before{content:"";position:absolute;left:0;top:3px;width:3px;height:3px;border-radius:50%;background:var(--brand-blue)}
.portrait{position:absolute;left:270px;top:36px;width:112px;height:514px;border-radius:50px 50px 6px 6px;background:linear-gradient(180deg,#e9e3dc 0%,#c9cfd8 20%,#2e3645 45%,#262d39 90%,#4a3a30 100%)}
</style>
</head>
<body>

<!-- Cover spread -->
<div class="spread spread--cover">
  <div class="page page--left back-cover">
    <div class="contact-bar">
      <div class="namemark namemark--small"><span class="namemark__square"></span>Marcus Hale</div>
      <ul class="contact-list">
        <li><svg viewBox="0 0 10 10"><circle cx="5" cy="5" r="5" fill="#1ba3dc"/><path d="M3.3 2.6l1 1-.5.7a4 4 0 0 0 1.9 1.9l.7-.5 1 1-.7.9C4.9 7.4 2.6 5.1 2.4 3.3z" fill="#fff"/></svg>+30 210 555 0181</li>
        <li><svg viewBox="0 0 10 10"><circle cx="5" cy="5" r="5" fill="#1ba3dc"/><path d="M3.3 2.6l1 1-.5.7a4 4 0 0 0 1.9 1.9l.7-.5 1 1-.7.9C4.9 7.4 2.6 5.1 2.4 3.3z" fill="#fff"/></svg>+30 214 555 0133</li>
        <li><svg viewBox="0 0 10 10"><rect x="1" y="2.5" width="8" height="5" fill="#1ba3dc"/><path d="M1 2.5l4 3 4-3" stroke="#fff" stroke-width=".8" fill="none"/></svg>info@northgateoffice.com</li>
      </ul>
      <ul class="contact-list">
        <li><svg viewBox="0 0 10 10"><circle cx="5" cy="5" r="5" fill="#1ba3dc"/><circle cx="5" cy="5" r="2.6" stroke="#fff" stroke-width=".7" fill="none"/><path d="M2.4 5h5.2" stroke="#fff" stroke-width=".7"/></svg>www.northgateoffice.com</li>
        <li><svg viewBox="0 0 10 10"><path d="M5 9.5S1.8 6 1.8 3.8a3.2 3.2 0 0 1 6.4 0C8.2 6 5 9.5 5 9.5z" fill="#1ba3dc"/><circle cx="5" cy="3.8" r="1.1" fill="#fff"/></svg>Keller Associates | Athens</li>
        <li style="padding-left:12px">Greece, Lysikratous 14-16</li>
        <li style="padding-left:12px">PO 105 58</li>
      </ul>
    </div>
  </div>

  <div class="page page--right front-cover">
    <svg class="layer" viewBox="0 0 396 560" width="396" height="560">
      <defs>
        <linearGradient id="photoTone" x1="0" y1="0" x2="1" y2="1">
          <stop offset="0" stop-color="#f6f6f6"/>
          <stop offset=".55" stop-color="#d2d2d2"/>
          <stop offset="1" stop-color="#e8e8e8"/>
        </linearGradient>
        <radialGradient id="discTone" cx=".45" cy=".4" r=".7">
          <stop offset="0" stop-color="#d9d9d9"/>
          <stop offset="1" stop-color="#9c9c9c"/>
        </radialGradient>
      </defs>
      <path d="M240 0H396V480Q360 448 250 452Z" fill="#1ba3dc"/>
      <path d="M0 0H282Q346 0 346 66V345Q346 448 246 452H0Z" fill="#fff"/>
      <rect y="452" width="396" height="108" fill="#fff"/>
      <path role="img" aria-label="Greyscale photo of a coach working with a young salesperson" d="M110 60H346V330Q300 360 200 320Q120 280 110 200Z" fill="url(#photoTone)" opacity=".9"/>
      <circle cx="250" cy="372" r="86" fill="url(#discTone)"/>
    </svg>
    <div class="namemark namemark--large"><span class="namemark__square"></span>Marcus Hale</div>
    <div class="namemark__sub">Halecoach Pacific Pty Ltd</div>
    <div class="cover-title">COACHING SESSION</div>
    <div class="cover-date">JUNE 2018</div>
    <div class="cover-url">www.mhsalescoach.com</div>
  </div>
</div>

<!-- Inner spread -->
<div class="spread spread--inner">
  <div class="page page--left">
    <div class="copy copy-left">
      <section>
        <h2>Yesterday – Today – Tomorrow</h2>
        <p>How many appraisals/listing presentations are booked in your diary for this week?</p>
        <p>How many appraisals/listing presentations are booked in your diary for next week?</p>
        <p>How many second viewings/private viewings are booked in your diary for this week?</p>
        <p>How many listings will you launch this week?</p>
      </section>
      <section>
        <h2>2018/2019 Productivity Gets</h2>
        <h3>There's more to it than numbers:</h3>
        <ol class="numbered">
          <li><b>1</b>Increase in market share in your core area</li>
          <li><b>2</b>Increase in commission rates</li>
          <li><b>3</b>Relationships [ data base growth]- future sellers</li>
          <li><b>4</b>Relationships [ data base growth] – buyer prospects</li>
          <li><b>5</b>Number of appointments/appraisals booked each week</li>
          <li><b>6</b>Listing pipeline growth</li>
          <li><b>7</b>Skills development –is an opportunity - you can't be defined as not knowing what to do. Be specific. You can't become a better closer if you don't have people to close on!!</li>
          <li><b>8</b>Managing free time – you can't be defined by time</li>
          <li><b>9</b>Time is an opportunity</li>
          <li><b>10</b>Know your data base system – data base is an opportunity</li>
          <li><b>11</b>Service charter – there is opportunity in service – repeat/referrals/the future seller calls "you in"</li>
          <li><b>12</b>Health &amp; energy leads to better recovery</li>
          <li><b>13</b>Family &amp; self- breaks</li>
          <li><b>14</b>Self-time</li>
          <li><b>15</b>Milestones/benchmarks</li>
          <li><b>16</b>Wealth creation</li>
        </ol>
      </section>
      <section>
        <h2>Today onwards [12/6/18]</h2>
        <p class="lead">Build the listing pipeline so you have shock coming to market when the sun shines again.</p>
      </section>
    </div>
  </div>

  <div class="page page--right">
    <div class="copy copy-right">
      <p class="lead">Don't wait until the usual "spring selling session" promo's start to start looking for listings.</p>
      <p class="lead">Get the jump on your competition by having your July to December profile building campaign set in place now &amp; make sure it is fully funded so you don't lose profile momentum.</p>
      <ol class="numbered">
        <li><b>1</b>What went well this month?</li>
        <li><b>2</b>Did you convert good days into good weeks, good weeks into a good month?</li>
        <li><b>3</b>How organised were you last week?</li>
        <li><b>4</b>What ideas, actions, processes, systems &amp; motivations have you introduced into your business during the last thirty days?</li>
        <li><b>5</b>What systems do you need to implement to</li>
        <li><b>6</b>create a smoother work flow?</li>
        <li><b>7</b>Are you pursuing what you believe in?</li>
        <li><b>8</b>At what time of the day are you running at</li>
        <li><b>9</b>your true potential?</li>
        <li><b>10</b>What have been your numbers for May?</li>
      </ol>
      <div class="bullets">
        <ul>
          <li>Speak to's</li><li>Appointments</li><li>Appraisals</li><li>Listing presentations</li>
          <li>Listing pipeline</li><li>Listing authorities signed</li><li>Listings launched</li><li>Home opens</li>
        </ul>
        <ul>
          <li>Negotiations</li><li>Sales</li><li>Lessons learned list</li>
          <li>Inroads into the market share in your core area – are you competitive, you when you are being called in.</li>
        </ul>
      </div>
      <ol class="numbered">
        <li><b>11</b>Script session – what was the best script you used last week?</li>
        <li><b>12</b>Stock review</li>
      </ol>
    </div>
    <div class="portrait" role="img" aria-label="Full-length photo of the coach in a navy suit and light blue shirt"></div>
  </div>
</div>

</body>
</html>
```